Redesign of Real Estate Agency Website

We need a redesign for our real estate agency website. Please see attached creative brief.

Target Market(s)

Refer to creative brief.

Industry/Entity Type

Real Estate

Requirements
Must have
• Refer to creative brief.

```html
<!DOCTYPE html>
<html lang="en">
<head>
<meta charset="utf-8">
<title>IslandKey – Phuket Property and Real Estate for Sale</title>
<link href="https://fonts.googleapis.com/css2?family=PT+Sans:wght@400;700&family=PT+Sans+Narrow:wght@400;700&display=swap" rel="stylesheet">
<style>
:root{
  --blue:#1a8ad8;
  --blue-dark:#0d6fb8;
  --blue-light:#4fb0ef;
  --navy:#1c2f5c;
  --orange:#f4a32a;
  --orange-dark:#c8490c;
  --link:#3a8fd8;
  --text:#333;
  --page:#ffffff;
}
*{margin:0;padding:0;box-sizing:border-box}
html,body{width:1024px;height:1200px;overflow:hidden}
body{background:linear-gradient(90deg,#cfcfcf 0,#f3f3f3 34px,var(--page) 40px,var(--page) 984px,#f3f3f3 990px,#cfcfcf 1024px);font-family:Arial,Helvetica,sans-serif;color:var(--text);position:relative}
.page-fade{position:absolute;left:40px;right:40px;top:880px;bottom:0;background:linear-gradient(#fff,#e4e6ea)}
.abs{position:absolute}
.brand{left:55px;top:26px;font-family:'PT Sans',sans-serif;font-size:26px;color:var(--navy);display:flex;align-items:center;gap:6px}
.brand i{width:12px;height:12px;border-radius:50%;background:var(--blue);display:block}
.tagline{left:228px;top:39px;font-size:13px;color:#333}
.cart{left:809px;top:21px;display:flex;gap:8px;font-size:11px;line-height:12px;color:#333}
.cart a{color:var(--link);text-decoration:none}
.nav{left:50px;top:66px;display:flex;gap:4px}
.nav span{width:129px;height:36px;border:1px solid #bbb;border-bottom:0;border-radius:3px 3px 0 0;background:linear-gradient(#fff,#dedede);font-family:'PT Sans Narrow',sans-serif;font-weight:700;font-size:15px;color:var(--navy);display:flex;align-items:center;justify-content:center;white-space:nowrap}
.nav span.active{background:linear-gradient(var(--blue-light),var(--blue));color:#fff;border-color:var(--blue)}
.crumbs{left:37px;top:102px;width:950px;height:31px;background:linear-gradient(var(--blue-light),var(--blue-dark));display:flex;gap:14px;padding-left:55px;align-items:center;font-family:'PT Sans Narrow',sans-serif;font-size:12px;color:#fff}
.crumbs span{text-decoration:underline}
.crumbs span::after{content:" ›";text-decoration:none}
.hero{left:57px;top:132px;width:911px;height:163px;border-radius:0 0 12px 12px;border:1px solid #9cc9e8;border-top:0;background:linear-gradient(#bcd9ec,#4ba3c9 60%,#2b8bb3)}
.hero-title{top:148px;font-family:'PT Sans Narrow',sans-serif;font-size:34px;letter-spacing:-.5px;color:#fff;text-shadow:0 1px 3px rgba(0,0,0,.4);white-space:nowrap}
.photo{border:5px solid #fff;box-shadow:0 2px 6px rgba(0,0,0,.35)}
.box{background:#fff;border:1px solid var(--blue);border-radius:10px;overflow:hidden}
.box h3{height:24px;background:linear-gradient(var(--blue-light),var(--blue));color:#fff;font-family:'PT Sans',sans-serif;font-weight:400;font-size:15px;line-height:24px;padding-left:16px;white-space:nowrap}
.side .box h3{font-family:'PT Sans Narrow',sans-serif;font-size:16px;padding-left:6px}
.side .box{box-shadow:0 1px 3px rgba(0,0,0,.15)}
.select{width:144px;height:18px;margin:8px 0 0 10px;border:1px solid #aaa;border-radius:3px;background:linear-gradient(#fff,#e9e9e9);font-family:'PT Sans Narrow',sans-serif;font-size:13px;color:var(--navy);padding-left:8px;line-height:16px;position:relative}
.select::after{content:"";position:absolute;right:-1px;top:-1px;width:14px;height:18px;background:var(--blue);border-radius:0 3px 3px 0}
.btn{display:block;margin:0 auto;width:90px;height:18px;border-radius:3px;background:linear-gradient(#ffc25a,var(--orange));color:#fff;font-family:'PT Sans',sans-serif;font-weight:700;font-size:13px;text-align:center;line-height:18px}
.small-link{font-family:'PT Sans Narrow',sans-serif;font-size:10px;line-height:11px;color:var(--link);text-align:center}
.browse li{list-style:none;font-family:'PT Sans Narrow',sans-serif;font-size:13.5px;color:var(--navy);line-height:20px;white-space:nowrap}
.pom h3,.hot h3{font-weight:700;font-size:14px;padding-left:8px}
.hot{border-color:var(--orange-dark)}
.hot h3{background:linear-gradient(#e3721f,var(--orange-dark));text-align:center;padding:0}
.pom-body{font-size:11px;line-height:14px}
.pom-body b{color:#222}
.pom-body a,.listing a{color:var(--link);text-decoration:none}
.listing{width:122px;font-size:11px;line-height:12px;white-space:nowrap}
.listing .img{width:120px;height:82px;border:1px solid #ccc;margin-bottom:4px}
.listing .name{color:var(--link);font-weight:700}
.intro{left:241px;top:952px;width:590px;font-family:'PT Sans',sans-serif;font-weight:700;font-size:13.5px;line-height:18px;color:var(--navy);white-space:nowrap}
.intro .lead{font-weight:400}
.footer{left:331px;top:1161px;font-family:'PT Sans Narrow',sans-serif;font-weight:700;font-size:12.5px;color:var(--navy)}
</style>
</head>
<body>
<div class="page-fade"></div>

<div class="abs brand"><i></i>IslandKey</div>
<div class="abs tagline">Phuket Property and Real Estate for Sale</div>
<div class="abs cart">
  <svg width="22" height="22" viewBox="0 0 22 22"><circle cx="11" cy="11" r="10" fill="none" stroke="#555"/><path d="M5 7h2l2 6h6l2-5H8" fill="none" stroke="#555" stroke-width="1.3"/><circle cx="10" cy="15.5" r="1" fill="#555"/><circle cx="14" cy="15.5" r="1" fill="#555"/></svg>
  <div>0 items in <a>sales inquiry cart</a><br>0 items in <a>rentals inquiry cart</a></div>
</div>

<nav class="abs nav">
  <span>Home</span><span class="active">Property for Sale</span><span>Property for Rent</span><span>Contact Us</span><span>About Us</span><span>List your Property</span><span>Property Buyer's Guide</span>
</nav>
<div class="abs crumbs"><span>home</span><span>for sale</span><span>villas &amp; houses</span><span>west phuket</span><span>kamala property</span><span>magnificent sea view villa</span></div>

<div class="abs hero" role="img" aria-label="Sea view through open white window shutters"></div>
<div class="abs hero-title" style="left:218px">Villa &amp; House for Sale</div>
<div class="abs hero-title" style="left:530px">Apartments &amp; Condos for Sale</div>
<div class="abs photo" style="left:237px;top:200px;width:281px;height:182px;background:linear-gradient(#8a8f96,#5a4434 60%,#2c2a2a)" role="img" aria-label="Evening photo of a Thai-style villa entrance with lit terrace"></div>
<div class="abs photo" style="left:531px;top:200px;width:278px;height:182px;background:linear-gradient(#e8eef2,#6fb9d8 50%,#2a8cb8)" role="img" aria-label="Modern apartment terrace with pool overlooking the bay"></div>

<div class="side">
  <div class="abs box" style="left:57px;top:300px;width:164px;height:216px">
    <h3 style="padding-left:15px">Quick Property Search</h3>
    <div class="select">Buy Property</div>
    <div class="select">Property Type</div>
    <div class="select">Region</div>
    <div class="select">District</div>
    <div class="select">Minimum Bedrooms</div>
    <div class="select">Maximum Price (THB)</div>
    <div style="margin-top:6px"><span class="btn">Search</span><div class="small-link">Advanced Search</div></div>
  </div>

  <div class="abs box" style="left:57px;top:524px;width:164px;height:249px;background:linear-gradient(#fff 80%,#d7ebf8)">
    <h3 style="text-align:center;padding:0">Search by map</h3>
    <div style="font-size:8px;color:#555;padding-left:52px;margin-top:6px">◉ Buy &nbsp;○ Rent</div>
    <div role="img" aria-label="Map of Phuket island divided into North, East, West, Town and South districts" style="margin:6px auto 0;width:110px;height:170px;border-radius:40% 50% 45% 40%;background:linear-gradient(#cfe6f7,#9ccbee)"></div>
    <div class="small-link" style="margin-top:12px">View large map</div>
  </div>

  <div class="abs box" style="left:57px;top:782px;width:164px;height:144px">
    <h3>Browse Property for Sale</h3>
    <ul class="browse" style="padding:6px 0 0 7px">
      <li>Hot Properties &amp; Promotions</li><li>Apartments &amp; Condos</li><li>Villas &amp; House</li><li>Commercial</li><li>Property Buyer's Guide</li>
    </ul>
  </div>

  <div class="abs box" style="left:57px;top:936px;width:164px;height:203px">
    <h3 style="text-align:center;padding:0">Get our newsletter</h3>
    <p style="font-family:'PT Sans Narrow',sans-serif;font-size:13px;line-height:12px;color:var(--navy);padding:11px 10px 0 12px">Get the latest Phuket Real Estate news and deals every month</p>
    <div style="margin:10px 0 0 10px;width:144px;height:18px;border:1px solid #aaa;border-radius:3px;font-size:13px;color:#bbb;padding-left:20px;line-height:16px;font-family:'PT Sans',sans-serif">Your email here</div>
    <div style="margin-top:15px"><span class="btn">Subscribe</span></div>
    <div style="font-size:9px;color:#777;margin:12px 0 0 16px">Privacy by <b style="color:#555">✓ MailSafe</b></div>
    <div style="margin:6px 0 0 20px;width:124px;height:14px;border:1px solid #bbb;border-radius:2px;background:#f4f4f4"></div>
  </div>
</div>

<svg class="abs" style="left:828px;top:301px" width="128" height="487" viewBox="0 0 128 487">
  <path d="M0 0H128V487L64 420L0 487Z" fill="#000"/>
</svg>

<div class="abs box pom" style="left:241px;top:396px;width:564px;height:171px">
  <h3>Property of the month</h3>
  <div class="pom-body" style="position:relative;height:140px">
    <div class="abs" role="img" aria-label="Residence building among green trees" style="left:16px;top:11px;width:122px;height:83px;border:1px solid #ccc;background:linear-gradient(#9fbf80,#4d7a3a)"></div>
    <div class="abs" style="left:145px;top:11px">
      <div style="color:var(--link);font-weight:700;font-size:12px">Banyan Grove Residence - 2 Bedroom</div>
      <div><b>Type:</b> Apartment/Condo</div>
      <div><b>Price:</b> <a>THB 7.6M</a></div>
      <div><b>Location:</b> Kamala, West Coast</div>
      <div><b>View:</b> Sea</div>
    </div>
    <p class="abs" style="left:16px;top:100px;width:540px">2-bedroom apartments offer 157 sqm, featuring quality local materials with natural finishes to create a relaxed and stylish living space. ... <a>view listing</a></p>
  </div>
</div>

<div class="abs box hot" style="left:241px;top:576px;width:564px;height:360px">
  <h3>Hot Villas for sale and Hot Apartments for Sale</h3>
</div>
<div class="abs listing" style="left:257px;top:608px"><div class="img" role="img" aria-label="Modern sea-view villa" style="background:linear-gradient(#d8d4cc,#6b5a48)"></div><div class="name">Luxury Sea-View ...</div>Natai<br>Villa<br>THB 45M</div>
<div class="abs listing" style="left:389px;top:608px"><div class="img" role="img" aria-label="Villa with garden lawn at night" style="background:linear-gradient(#c9c39a,#4f6a2e)"></div><div class="name">The Royal Estate ...</div>Layan<br>Villa<br>THB 16.9M - 17.7M</div>
<div class="abs listing" style="left:534px;top:608px"><div class="img" role="img" aria-label="Beachfront pool under trees" style="background:linear-gradient(#5c8a6a,#4db2d0)"></div><div class="name">Oceanfront Suite ...</div>Bangtao<br>Apartment/Condo<br>THB 27M</div>
<div class="abs listing" style="left:667px;top:608px"><div class="img" role="img" aria-label="Open living room facing the sea" style="background:linear-gradient(90deg,#3a3631,#bcd8e0 50%,#3a3631)"></div><div class="name">2-Bed Foreign ...</div>Kata<br>Apartment/Condo<br>THB 18.5M - 25M</div>

<div class="abs listing" style="left:254px;top:760px"><div class="img" role="img" aria-label="Villa pool lit at dusk" style="background:linear-gradient(#2a3f78,#d08a3a 70%,#3b8fc0)"></div><div class="name">Naiharn Palms ...</div>Nai Harn<br>Villa<br>THB 12M - 15M</div>
<div class="abs listing" style="left:387px;top:760px"><div class="img" role="img" aria-label="Thai-style villa with pool" style="background:linear-gradient(#c9e0ee,#a05a34 55%,#4fa6c6)"></div><div class="name">4 Bedroom Naiharn ...</div>Nai Harn<br>Villa<br>THB 14.9M - 17.49M</div>
<div class="abs listing" style="left:534px;top:760px"><div class="img" role="img" aria-label="White apartment towers and palms" style="background:linear-gradient(#cfe3f2,#e6e6e6 60%,#6f9a5a)"></div><div class="name">Karon Ridge ...</div>Karon<br>Apartment/Condo<br>THB 3.5M - 31.3M</div>
<div class="abs listing" style="left:667px;top:760px"><div class="img" role="img" aria-label="Condominium building with lawn" style="background:linear-gradient(#e4edf3,#c9c2b4 55%,#5f8c45)"></div><div class="name">Coral Sands ...</div>Mai Khao<br>Apartment/Condo<br>THB 9.9M - 38.9M</div>
<div class="abs" style="left:671px;top:903px;font-size:11px;color:var(--link)">View all hot properties &gt;&gt;</div>

<div class="abs intro">
  <div class="lead">IslandKey Real Estate Agents</div>
  Whether you are searching for a beachfront villa, sea view apartment or an exciting investment<br>
  opportunity we can help you find your ideal Phuket property. We have selected the finest<br>
  that Phuket has to offer. Our highly experienced sales team is available to provide further<br>
  details on any Phuket property for sale and we would be delighted to arrange viewings.<br>
  Please contact us with your Phuket real estate requirements.
</div>

<div class="abs footer">Phuket Real Estate from IslandKey | Copyright © IslandKey 2008. All Rights Reserved</div>
<div class="abs" style="left:894px;top:1159px;font-family:'PT Sans Narrow',sans-serif;font-weight:700;font-size:14px;color:var(--navy)">Top ⌃</div>
</body>
</html>
```